FestivaLoom Business Cards

Front
Has logo with a design. Website address (www.festivaloom-demo.com)
Has slogan (celebrate every night)
Has phone number (5559183047)
Should be bold and stands out.

Back
Has details about what we offer.

Events
Search upcoming events
Submit events
Party Image Gallery
View and download HQ party images
Sign up as a contributing event photographer and get paid!
Tickets
Sell your event tickets online for free!
Direct pay
No ticket fee

Target Market(s)

These cards will be handed out in clubs and events to patrons.

Industry/Entity Type

Business

Contact Information for Business Card

Should match or mirror our website in some sort of way. Visit the website to get ideas.

Requirements
Must have
• Must be designed for a 3x3 inch card.

```html
<!DOCTYPE html>
<html lang="en">
<head>
<meta charset="utf-8">
<title>FestivaLoom Business Cards</title>
<link href="https://fonts.googleapis.com/css2?family=Open+Sans:wght@400;600;700&display=swap" rel="stylesheet">
<style>
  :root {
    --stage: #2f2f2f;
    --card: #ffffff;
    --blue: #2fa3d8;
    --pink: #e0408f;
    --text: #555555;
  }
  * { box-sizing: border-box; margin: 0; padding: 0; }
  html, body {
    width: 1200px; height: 750px; overflow: hidden;
    background: var(--stage);
    font-family: "Open Sans", sans-serif;
  }
  .card {
    position: absolute; top: 166px;
    width: 416px; height: 416px;
    background: var(--card);
  }
  .card--front { left: 170px; }
  .card--back { left: 619px; }

  .brand {
    position: absolute; top: 44px; left: 52px;
    display: flex; align-items: center; gap: 12px;
  }
  .brand__mark { width: 40px; height: 40px; background: var(--blue); }
  .brand__name {
    font-size: 30px; font-weight: 600; color: var(--blue); line-height: 1;
  }
  .brand__slogan {
    position: absolute; top: 82px; left: 104px; width: 258px;
    font-size: 11px; letter-spacing: 4.2px; color: #333; text-align: left;
  }
  .phone {
    position: absolute; top: 126px; left: 0; width: 100%;
    text-align: center; font-size: 52px; font-weight: 600;
    color: var(--blue); line-height: 1.2;
  }
  .website {
    position: absolute; top: 180px; left: 0; width: 100%;
    text-align: center; font-size: 24px; font-weight: 700;
    color: var(--pink); line-height: 1.2;
  }
  .equalizer {
    position: absolute; left: 8px; top: 240px;
    width: 402px; height: 170px;
    background: linear-gradient(180deg, var(--pink) 0%, var(--pink) 38%, var(--blue) 62%, var(--blue) 100%);
    opacity: 0.9;
  }

  .emblem {
    position: absolute; left: 255px; top: 28px;
    width: 116px; height: 116px; border-radius: 50%;
    background: var(--blue);
  }
  .offer { position: absolute; left: 32px; top: 160px; }
  .offer__title {
    font-size: 18px; font-weight: 700; color: var(--blue); margin-bottom: 6px;
  }
  .offer__list { list-style: none; }
  .offer__item {
    position: relative; padding-left: 16px;
    font-size: 13.5px; color: var(--text); line-height: 22.2px;
  }
  .offer__item::before {
    content: ""; position: absolute; left: 2px; top: 9px;
    width: 5px; height: 5px; border-radius: 50%; background: var(--blue);
  }
</style>
</head>
<body>
  <section class="card card--front">
    <div class="brand">
      <span class="brand__mark"></span>
      <span class="brand__name">FestivaLoom</span>
    </div>
    <p class="brand__slogan">celebrate every night</p>
    <p class="phone">5559183047</p>
    <p class="website">www.festivaloom-demo.com</p>
    <div class="equalizer" role="img" aria-label="Pink and blue equalizer bar decoration"></div>
  </section>

  <section class="card card--back">
    <div class="emblem"></div>
    <div class="offer">
      <h2 class="offer__title">Events</h2>
      <ul class="offer__list">
        <li class="offer__item">Search upcoming events</li>
        <li class="offer__item">Submit events</li>
        <li class="offer__item">Party Image Gallery</li>
        <li class="offer__item">View and download HQ party images</li>
        <li class="offer__item">Sign up as a contributing event photographer &amp; get paid!</li>
        <li class="offer__item">Tickets</li>
        <li class="offer__item">Sell your event tickets online for free!</li>
        <li class="offer__item">Direct pay</li>
        <li class="offer__item">No ticket fee</li>
      </ul>
    </div>
  </section>
</body>
</html>
```